Promotional Banner Redesign - Multi-Size

We need a professional promotional banner designed in three sizes:
1080×1080
1920×1080
1080×1920

Please use the attached layered PSD file as your starting point. It contains all required elements:
Copy (text)
Logos
Images / visual assets
Existing layout reference

What We Want:
The current design has the right theme, but it is too visually cluttered.
We need a cleaner, more modern, more readable, and more balanced reinterpretation of the same concept — something that still feels energetic and on-brand, but with better visual hierarchy and readability.

Your redesign can be somewhat different in layout and visual treatment, as long as it keeps the same general look/feel and communicates the same promotional message.

Feel free to take creative liberties as long as the theme and core messaging remain consistent.

This banner will be used on:
High-resolution streaming platform placements
FAST channel home screens
Paid ads
Social media
Print / event displays

So it must look excellent across all mediums.

Deliverables:
You will provide one design, exported in all required sizes:
1080×1080 JPG
1920×1080 JPG
1080×1920 JPG

AND:

Source Files:
Fully editable layered PSD file

All fonts used must be from one or more of the following:
Quillmark Type
Brindle Glyphs
Marrowvale Assets licensed

Please include:
Font download links
Any stock photo links (must be commercially licensed for broadcast with no time limit)

Notes & Expectations:
The design must be clean, bold, and professional, with strong text hierarchy.

The theme should remain consistent with the original PSD, but feel free to simplify, modernize, or re-organize the layout.

Designers with experience in streaming thumbnail layout, motion graphics, or broadcast design are encouraged to apply.

We are actively searching for a designer we can work with on a long-term basis. We create many show banners and streaming thumbnails, so ongoing work is likely for the right designer.

Optional:
If you would like to show multiple design variations, please feel free — this will strengthen your proposal.

Questions?
Please message us with any questions you need answered before or during the project. We’re happy to clarify!

Streaming TV Viewers

Streaming TV

0054AA
0677BA
7BADD7
CADEEF
E8F1F8
EB3D1F
EC4F4E
F09395
F8D3D4
FCEDEE

• See the brief
• That Vexlo look - no no no

```html
<!DOCTYPE html>
<html lang="en">
<head>
<meta charset="utf-8">
<title>Streaming Marathon Banners – Three Sizes</title>
<link rel="stylesheet" href="https://fonts.googleapis.com/css2?family=Anton&family=Bebas+Neue&family=Courgette&family=Poppins:ital,wght@0,400;0,600;0,700;0,800;1,700&display=swap">
<style>
  :root{
    --sheet:#b9b9b9;
    --navy:#1a3563;
    --red:#d7191f;
    --white:#ffffff;
    --city:#e6e8ec;
    --label:#1c1c1c;
  }
  *{margin:0;padding:0;box-sizing:border-box}
  html,body{width:761px;height:1200px;overflow:hidden;background:var(--sheet)}
  .sheet{position:relative;width:761px;height:1200px}

  .banner{position:absolute;overflow:hidden;background:linear-gradient(180deg,var(--white) 20%,var(--city) 70%,var(--white));font-family:"Poppins",sans-serif;color:var(--navy)}
  .banner--wide{left:122px;top:109px;width:507px;height:284px}
  .banner--square{left:413px;top:535px;width:285px;height:284px}
  .banner--tall{left:63px;top:535px;width:285px;height:506px}

  .size-label{position:absolute;font:italic 700 30px/1 "Poppins",sans-serif;color:var(--label);text-align:center;width:260px}
  .size-label--wide{left:245px;top:414px}
  .size-label--square{left:424px;top:843px}
  .size-label--tall{left:75px;top:1061px}

  .flag,.portrait,.band{position:absolute;left:0;top:0}

  .logo-row{position:absolute;display:flex;align-items:center;justify-content:space-between}
  .logo-name{font:700 8px/1 "Poppins",sans-serif;color:var(--navy);white-space:nowrap}
  .logo-name--red{color:var(--red)}

  .big-s{position:absolute;font-family:"Anton",sans-serif;line-height:1;background:linear-gradient(180deg,var(--navy) 45%,var(--red) 85%);-webkit-background-clip:text;background-clip:text;color:transparent}
  .kicker{position:absolute;font-weight:700;color:var(--red);line-height:1;white-space:nowrap}
  .title{position:absolute;font-family:"Anton",sans-serif;line-height:1;white-space:nowrap;background:linear-gradient(180deg,var(--navy) 40%,var(--red));-webkit-background-clip:text;background-clip:text;color:transparent}
  .tagline{position:absolute;font-family:"Courgette",cursive;color:var(--navy);line-height:1.2;white-space:nowrap}
  .weekend{position:absolute;font-weight:800;color:var(--navy);line-height:1.05;white-space:nowrap}

  .date{position:absolute;text-align:center;border-radius:2px;overflow:hidden;font-family:"Bebas Neue",sans-serif}
  .date-month{display:block;background:var(--red);color:var(--white);font-family:"Poppins",sans-serif;font-weight:600}
  .date-day{display:block;background:var(--navy);color:var(--white)}
  .date-day sup{font-size:55%}
  .date-to{position:absolute;border-radius:50%;background:#222;color:var(--white);border:1.5px solid var(--white);box-shadow:0 0 0 1px #222;font:600 6px/1 "Poppins",sans-serif;display:flex;align-items:center;justify-content:center}

  .time{position:absolute;font-weight:700;color:var(--red);white-space:nowrap;line-height:1}
  .time small{font-size:70%}
  .time .to{color:var(--navy)}
  .zone{position:absolute;font-weight:600;color:var(--navy);letter-spacing:.04em;line-height:1;white-space:nowrap}
  .divider{position:absolute;width:1px;background:#9aa4b5}

  .stream{position:absolute;font-family:"Anton",sans-serif;line-height:1.05;color:var(--navy);white-space:nowrap}
  .stream b{font-weight:400;color:var(--red)}
  .network{position:absolute;display:flex;align-items:center;gap:3px;font:700 5px/1 "Poppins",sans-serif;color:var(--navy);white-space:nowrap}
  .network-dot{border-radius:50%;border:1.5px solid var(--red);background:var(--white)}

  .feature{position:absolute;color:var(--white);white-space:nowrap;line-height:1.15}
  .feature-intro{font-weight:400}
  .feature-name{font-weight:700}
  .feature-role{font-weight:700}

  /* wide */
  .banner--wide .logo-row{left:270px;top:26px;width:216px}
  .banner--wide .big-s{left:199px;top:38px;font-size:80px}
  .banner--wide .kicker{left:243px;top:59px;font-size:17px}
  .banner--wide .title{left:243px;top:78px;font-size:29px}
  .banner--wide .tagline{left:207px;top:114px;font-size:13px}
  .banner--wide .weekend{left:206px;top:134px;font-size:16px}
  .banner--wide .date{width:29px;top:157px}
  .banner--wide .date-month{font-size:8px;line-height:11px}
  .banner--wide .date-day{font-size:14px;line-height:22px}
  .banner--wide .date--start{left:206px}
  .banner--wide .date--end{left:254px}
  .banner--wide .date-to{left:237px;top:168px;width:14px;height:14px}
  .banner--wide .divider{left:294px;top:157px;height:36px}
  .banner--wide .time{left:306px;top:155px;font-size:17px}
  .banner--wide .zone{left:306px;top:174px;font-size:19px}
  .banner--wide .stream{left:206px;top:201px;font-size:17px}
  .banner--wide .network{left:302px;top:198px}
  .banner--wide .network-dot{width:26px;height:26px}
  .banner--wide .feature{left:206px;top:236px}
  .banner--wide .feature-intro{font-size:9px}
  .banner--wide .feature-name{font-size:13px}
  .banner--wide .feature-role{font-size:6px}

  /* square */
  .banner--square .logo-row{left:135px;top:21px;width:130px}
  .banner--square .logo-name{font-size:5.5px}
  .banner--square .big-s{left:134px;top:44px;font-size:50px}
  .banner--square .kicker{left:164px;top:50px;font-size:14px}
  .banner--square .title{left:161px;top:66px;font-size:24px}
  .banner--square .title--second{left:135px;top:89px}
  .banner--square .tagline{left:135px;top:118px;font-size:11px}
  .banner--square .weekend{left:135px;top:154px;font-size:11px}
  .banner--square .date{width:19px;top:171px}
  .banner--square .date-month{font-size:5px;line-height:7px}
  .banner--square .date-day{font-size:9.5px;line-height:15px}
  .banner--square .date--start{left:135px}
  .banner--square .date--end{left:169px}
  .banner--square .date-to{left:156px;top:178px;width:10px;height:10px;font-size:4px}
  .banner--square .time{left:205px;top:170px;font-size:11px}
  .banner--square .zone{left:205px;top:182px;font-size:13px}
  .banner--square .stream{left:135px;top:205px;font-size:17px}
  .banner--square .network{left:229px;top:198px;flex-direction:column;gap:2px;font-size:4px}
  .banner--square .network-dot{width:22px;height:22px}
  .banner--square .feature{left:135px;top:243px}
  .banner--square .feature-intro{font-size:8.5px}
  .banner--square .feature-name{font-size:12.5px}
  .banner--square .feature-role{font-size:5.5px}

  /* tall */
  .banner--tall .logo-row{left:104px;top:27px;width:158px}
  .banner--tall .logo-name{font-size:6.5px}
  .banner--tall .big-s{left:99px;top:56px;font-size:78px}
  .banner--tall .kicker{left:142px;top:82px;font-size:17px}
  .banner--tall .title{left:142px;top:100px;font-size:30px}
  .banner--tall .title--second{left:105px;top:131px}
  .banner--tall .tagline{left:104px;top:171px;font-size:13px}
  .banner--tall .weekend{left:175px;top:213px;font-size:13px}
  .banner--tall .date{width:23px;top:250px}
  .banner--tall .date-month{font-size:6px;line-height:9px}
  .banner--tall .date-day{font-size:11.5px;line-height:18px}
  .banner--tall .date--start{left:175px}
  .banner--tall .date--end{left:214px}
  .banner--tall .date-to{left:200px;top:258px;width:12px;height:12px;font-size:5px}
  .banner--tall .time{left:175px;top:285px;font-size:13px}
  .banner--tall .zone{left:175px;top:299px;font-size:15px}
  .banner--tall .stream{left:175px;top:323px;font-size:15px}
  .banner--tall .network{left:222px;top:326px;flex-direction:column;gap:2px;font-size:4.5px}
  .banner--tall .network-dot{width:30px;height:30px}
  .banner--tall .feature{left:104px;top:439px}
  .banner--tall .feature-intro{font-size:11px}
  .banner--tall .feature-name{font-size:17px}
  .banner--tall .feature-role{font-size:7.5px}
</style>
</head>
<body>
<main class="sheet">

  <!-- 1920 x 1080 -->
  <section class="banner banner--wide">
    <svg class="flag" width="507" height="284" viewBox="0 0 507 284" role="img" aria-label="Waving American flag in the top-left and bottom-right corners">
      <defs>
        <linearGradient id="flagWideA" x1="0" y1="0" x2="1" y2="1"><stop offset="0" stop-color="#1c3470"/><stop offset=".55" stop-color="#d7262d"/><stop offset="1" stop-color="#f3d8d8"/></linearGradient>
        <linearGradient id="flagWideB" x1="1" y1="0" x2="0" y2="1"><stop offset="0" stop-color="#1c3470"/><stop offset=".6" stop-color="#d7262d"/><stop offset="1" stop-color="#f3dada"/></linearGradient>
      </defs>
      <polygon points="0,0 172,0 120,70 60,120 0,150" fill="url(#flagWideA)"/>
    </svg>
    <svg class="portrait" width="507" height="284" viewBox="0 0 507 284" role="img" aria-label="Portrait of the featured host, arms crossed, in a navy blazer and light blue shirt">
      <defs><linearGradient id="hostWide" x1="0" y1="0" x2="0" y2="1"><stop offset="0" stop-color="#c99a83"/><stop offset=".35" stop-color="#7fd6f2"/><stop offset=".5" stop-color="#1f3360"/><stop offset="1" stop-color="#182a52"/></linearGradient></defs>
      <path d="M40,40 Q80,25 105,45 L110,110 Q150,120 162,170 L162,284 L0,284 L0,140 Q20,115 50,110 Z" fill="url(#hostWide)"/>
    </svg>
    <svg class="band" width="507" height="284" viewBox="0 0 507 284">
      <polygon points="190,234 507,234 507,284 70,284" fill="var(--navy)"/>
      <path d="M60,284 Q110,248 176,234 L172,227 L197,224 L186,248 L182,241 Q120,252 60,284 Z" fill="var(--red)"/>
      <polygon points="507,112 507,284 347,284 410,230 470,160" fill="url(#flagWideB)"/>
    </svg>
    <div class="logo-row"><span class="logo-name">Past the Deal</span><span class="logo-name logo-name--red">The Grand Unveil</span><span class="logo-name">Surge Nation</span></div>
    <div class="big-s">S</div>
    <div class="kicker">Surge In 2026</div>
    <div class="title">TREAMING MARATHON!</div>
    <div class="tagline">Learn From Real Founders Making It Happen!</div>
    <div class="weekend">NEW YEAR’S WEEKEND</div>
    <div class="date date--start"><span class="date-month">DEC</span><span class="date-day">31<sup>ST</sup></span></div>
    <div class="date-to">TO</div>
    <div class="date date--end"><span class="date-month">DEC</span><span class="date-day">04<sup>TH</sup></span></div>
    <div class="divider"></div>
    <div class="time">2<small>PM</small> <small class="to">TO</small> 8<small>PM</small></div>
    <div class="zone">EASTERN</div>
    <div class="stream">STREAM <b>FREE!</b></div>
    <div class="network"><span class="network-dot"></span>Hometown Tales</div>
    <div class="feature"><div class="feature-intro">Featuring the Iconic</div><div class="feature-name">Dale Whitmore</div><div class="feature-role">Original Shark from Fin Pitch</div></div>
  </section>
  <div class="size-label size-label--wide">1920 x 1080</div>

  <!-- 1080 x 1920 -->
  <section class="banner banner--tall">
    <svg class="flag" width="285" height="506" viewBox="0 0 285 506" role="img" aria-label="Waving American flag across the top-left corner">
      <defs><linearGradient id="flagTall" x1="0" y1="0" x2="1" y2="1"><stop offset="0" stop-color="#1c3470"/><stop offset=".55" stop-color="#d7262d"/><stop offset="1" stop-color="#f3d8d8"/></linearGradient></defs>
      <polygon points="0,0 120,0 95,50 55,100 0,150" fill="url(#flagTall)"/>
    </svg>
    <svg class="portrait" width="285" height="506" viewBox="0 0 285 506" role="img" aria-label="Portrait of the featured host, arms crossed, in a navy blazer and light blue shirt">
      <defs><linearGradient id="hostTall" x1="0" y1="0" x2="0" y2="1"><stop offset="0" stop-color="#c99a83"/><stop offset=".3" stop-color="#7fd6f2"/><stop offset=".45" stop-color="#1f3360"/><stop offset="1" stop-color="#182a52"/></linearGradient></defs>
      <path d="M15,130 Q60,105 85,125 L90,210 Q150,225 165,300 L165,470 L0,485 L0,230 Q10,215 25,212 Z" fill="url(#hostTall)"/>
    </svg>
    <svg class="band" width="285" height="506" viewBox="0 0 285 506">
      <polygon points="222,381 285,381 285,506 0,506 0,488 200,412" fill="var(--navy)"/>
      <path d="M0,482 Q90,425 190,402 L184,393 L224,377 L206,420 L200,410 Q100,440 0,490 Z" fill="var(--red)"/>
    </svg>
    <div class="logo-row"><span class="logo-name">Past the Deal</span><span class="logo-name logo-name--red">Grand Unveil</span><span class="logo-name">Surge Nation</span></div>
    <div class="big-s">S</div>
    <div class="kicker">Surge In 2026</div>
    <div class="title">TREAMING</div>
    <div class="title title--second">MARATHON!</div>
    <div class="tagline">Learn From Real Founders<br>Making It Happen!</div>
    <div class="weekend">NEW YEAR’S<br>WEEKEND</div>
    <div class="date date--start"><span class="date-month">DEC</span><span class="date-day">31<sup>ST</sup></span></div>
    <div class="date-to">TO</div>
    <div class="date date--end"><span class="date-month">DEC</span><span class="date-day">04<sup>TH</sup></span></div>
    <div class="time">2<small>PM</small> <small class="to">TO</small> 8<small>PM</small></div>
    <div class="zone">EASTERN</div>
    <div class="stream">STREAM<br><b>FREE!</b></div>
    <div class="network"><span class="network-dot"></span>Hometown Tales</div>
    <div class="feature"><div class="feature-intro">Featuring the Iconic</div><div class="feature-name">Dale Whitmore</div><div class="feature-role">Original Shark from Fin Pitch</div></div>
  </section>
  <div class="size-label size-label--tall">1080 x 1920</div>

  <!-- 1080 x 1080 -->
  <section class="banner banner--square">
    <svg class="flag" width="285" height="284" viewBox="0 0 285 284" role="img" aria-label="Waving American flag across the top-left corner">
      <defs><linearGradient id="flagSquare" x1="0" y1="0" x2="1" y2="1"><stop offset="0" stop-color="#1c3470"/><stop offset=".55" stop-color="#d7262d"/><stop offset="1" stop-color="#f3d8d8"/></linearGradient></defs>
      <polygon points="0,0 142,0 100,40 60,70 0,95" fill="url(#flagSquare)"/>
    </svg>
    <svg class="portrait" width="285" height="284" viewBox="0 0 285 284" role="img" aria-label="Portrait of the featured host, arms crossed, in a navy blazer and light blue shirt">
      <defs><linearGradient id="hostSquare" x1="0" y1="0" x2="0" y2="1"><stop offset="0" stop-color="#c99a83"/><stop offset=".35" stop-color="#7fd6f2"/><stop offset=".5" stop-color="#1f3360"/><stop offset="1" stop-color="#182a52"/></linearGradient></defs>
      <path d="M15,40 Q50,25 68,42 L70,105 Q115,115 124,175 L124,262 L0,276 L0,120 Q10,105 25,103 Z" fill="url(#hostSquare)"/>
    </svg>
    <svg class="band" width="285" height="284" viewBox="0 0 285 284">
      <polygon points="120,239 285,239 285,284 12,284 112,252" fill="var(--navy)"/>
      <path d="M6,284 Q60,258 112,248 L108,240 L128,244 L114,258 L114,252 Q60,264 6,284 Z" fill="var(--red)"/>
    </svg>
    <div class="logo-row"><span class="logo-name">Past the Deal</span><span class="logo-name logo-name--red">Grand Unveil</span><span class="logo-name">Surge Nation</span></div>
    <div class="big-s">S</div>
    <div class="kicker">Surge In 2026</div>
    <div class="title">TREAMING</div>
    <div class="title title--second">MARATHON!</div>
    <div class="tagline">Learn From Real Founders<br>Making It Happen!</div>
    <div class="weekend">NEW YEAR’S WEEKEND</div>
    <div class="date date--start"><span class="date-month">DEC</span><span class="date-day">31<sup>ST</sup></span></div>
    <div class="date-to">TO</div>
    <div class="date date--end"><span class="date-month">DEC</span><span class="date-day">04<sup>TH</sup></span></div>
    <div class="time">2<small>PM</small> <small class="to">TO</small> 8<small>PM</small></div>
    <div class="zone">EASTERN</div>
    <div class="stream">STREAM <b>FREE!</b></div>
    <div class="network"><span class="network-dot"></span>Hometown Tales</div>
    <div class="feature"><div class="feature-intro">Featuring the Iconic</div><div class="feature-name">Dale Whitmore</div><div class="feature-role">Original Shark from Fin Pitch</div></div>
  </section>
  <div class="size-label size-label--square">1080 x 1080</div>

</main>
</body>
</html>
```